Bright Lane Collective needs updated website.

Our current website was designed on wix.com. (www.brightlanecollective.example).
We would like something a little more customized for what our company offers. Bright Lane Collective is a company specializing in connecting consumers with trustworthy and affordable service professionals. We need the website to be approachable and easy to use, while conveying our "Bright Lane" reputation.
Reason: Our project is now guaranteed. Please send your ideas. Thank you!
Target Market(s)
Homeowners
Industry/Entity Type
It Company
Look and feel

```html
<!DOCTYPE html>
<html lang="en">
<head>
<meta charset="utf-8">
<title>Contact Us – Bright Lane Collective</title>
<link rel="stylesheet" href="https://fonts.googleapis.com/css2?family=Source+Sans+3:wght@400;600;700&display=swap">
<style>
  :root {
    --green: #82b22c;
    --green-dark: #57860e;
    --green-light: #c6ea8c;
    --text: #4a4a4a;
    --text-soft: #5a5a5a;
    --rule: #d8d8d8;
    --field-border: #c9c9c9;
    --field-top: #ececec;
    --field-bottom: #f8f8f8;
    --map-light: #e4e4e4;
    --map-mid: #d6d8dc;
    --white: #ffffff;
  }
  * { box-sizing: border-box; margin: 0; padding: 0; }
  html, body { width: 1200px; height: 1064px; overflow: hidden; }
  body {
    position: relative;
    background: var(--white);
    font-family: "Source Sans 3", sans-serif;
    color: var(--text);
  }

  /* Header */
  .site-header { position: absolute; left: 0; top: 0; width: 1200px; height: 167px; border-bottom: 1px solid var(--green); }
  .brand { position: absolute; left: 104px; top: 64px; display: flex; align-items: center; gap: 12px; }
  .brand-dot { width: 40px; height: 40px; border-radius: 50%; background: var(--green); }
  .brand-name { font-size: 34px; font-weight: 700; color: var(--text); letter-spacing: -0.5px; }
  .call-box { position: absolute; left: 882px; top: 49px; }
  .call-label { font-size: 23px; line-height: 28px; color: var(--text-soft); }
  .call-number { font-size: 30px; line-height: 36px; font-weight: 700; color: var(--text); }

  /* Navigation */
  .main-nav { position: absolute; left: 0; top: 167px; width: 1200px; height: 70px; border-bottom: 1px solid var(--rule); }
  .nav-link { position: absolute; top: 0; height: 69px; line-height: 63px; font-size: 20px; color: var(--text-soft); text-decoration: none; text-align: center; }
  .nav-sep { position: absolute; top: 20px; height: 28px; border-left: 1px dotted #c8c8c8; }
  .nav-link.is-active { background: var(--green); color: var(--white); font-weight: 700; left: 926px; width: 168px; }

  /* Contact info */
  .map-area { position: absolute; left: 104px; top: 262px; width: 422px; height: 315px;
    background: linear-gradient(135deg, var(--map-light), var(--map-mid)); }
  .address { position: absolute; left: 104px; top: 595px; font-size: 17px; font-weight: 700; line-height: 24px; color: var(--text); }
  .contact-list { position: absolute; left: 104px; top: 667px; font-size: 17px; line-height: 24px; color: var(--text-soft); }
  .contact-row { display: flex; }
  .contact-row dt { width: 105px; }

  /* Form */
  .contact-form { position: absolute; left: 647px; top: 257px; width: 447px; }
  .form-title { font-size: 17px; line-height: 22px; font-weight: 700; color: var(--text); margin-bottom: 17px; }
  .field { display: block; width: 300px; height: 31px; margin-bottom: 10px; border: 1px solid var(--field-border);
    background: linear-gradient(var(--field-top), var(--field-bottom)); padding: 0 9px; font: 13px "Source Sans 3", sans-serif; color: #888; }
  .field::placeholder { color: #888; }
  .field-message { width: 447px; height: 268px; margin-top: 0; margin-bottom: 0; padding-top: 9px; resize: none; }
  .submit-btn { display: block; margin-top: 8px; width: 108px; height: 43px; border: 0; background: var(--green);
    color: var(--white); font: 18px "Source Sans 3", sans-serif; }

  /* Footer */
  .site-footer { position: absolute; left: 0; top: 832px; width: 1200px; height: 232px; background: var(--green-dark); color: var(--white); }
  .footer-brand { position: absolute; left: 106px; top: 48px; display: flex; align-items: center; gap: 10px; }
  .footer-brand .brand-dot { width: 34px; height: 34px; background: var(--white); }
  .footer-brand .brand-name { font-size: 26px; color: var(--white); }
  .copyright { position: absolute; left: 106px; top: 116px; font-size: 13px; }
  .footer-nav { position: absolute; right: 105px; top: 34px; display: flex; gap: 29px; font-size: 13px; }
  .footer-nav a { color: var(--white); text-decoration: none; }
  .footer-address { position: absolute; right: 105px; top: 81px; font-size: 17px; }
  .footer-phone { position: absolute; right: 105px; top: 124px; font-size: 22px; color: var(--green-light); }
  .footer-email { position: absolute; right: 105px; top: 154px; font-size: 17px; }
</style>
</head>
<body>
  <header class="site-header">
    <div class="brand">
      <span class="brand-dot"></span>
      <span class="brand-name">Bright Lane Collective</span>
    </div>
    <div class="call-box">
      <div class="call-label">Call Us Now:</div>
      <div class="call-number">1-555-014-2270</div>
    </div>
  </header>

  <nav class="main-nav">
    <a class="nav-link" href="#" style="left:140px;width:92px">HOME</a>
    <span class="nav-sep" style="left:253px"></span>
    <a class="nav-link" href="#" style="left:280px;width:196px">ABOUT BRIGHT LANE</a>
    <span class="nav-sep" style="left:501px"></span>
    <a class="nav-link" href="#" style="left:530px;width:112px">SERVICES</a>
    <span class="nav-sep" style="left:670px"></span>
    <a class="nav-link" href="#" style="left:700px;width:158px">OUR NETWORK</a>
    <a class="nav-link is-active" href="#">CONTACT US</a>
  </nav>

  <main>
    <div class="map-area" role="img" aria-label="Street map showing the office location"></div>
    <p class="address">412 Harbor Street<br>Riverton, Ohio 43210</p>
    <dl class="contact-list">
      <div class="contact-row"><dt>Telephone:</dt><dd>+1 555 010 4481</dd></div>
      <div class="contact-row"><dt>FAX:</dt><dd>+1 555 010 7732</dd></div>
      <div class="contact-row"><dt>E-mail:</dt><dd>mail@brightlanecollective.example</dd></div>
    </dl>

    <form class="contact-form">
      <h2 class="form-title">Contact Form</h2>
      <input class="field" type="text" placeholder="Name:">
      <input class="field" type="email" placeholder="E-mail:">
      <input class="field" type="tel" placeholder="Phone:">
      <textarea class="field field-message" placeholder="Message:"></textarea>
      <button class="submit-btn" type="button">Submit</button>
    </form>
  </main>

  <footer class="site-footer">
    <div class="footer-brand">
      <span class="brand-dot"></span>
      <span class="brand-name">Bright Lane Collective</span>
    </div>
    <p class="copyright">© copyrights Bright Lane Collective Inc. All rights reserved</p>
    <nav class="footer-nav">
      <a href="#">Home</a>
      <a href="#">About bright lane</a>
      <a href="#">Services</a>
      <a href="#">Our network</a>
      <a href="#">Contact us</a>
    </nav>
    <p class="footer-address">412 Harbor Street, Riverton, Ohio 43210</p>
    <p class="footer-phone">Phone: 1-555-014-2270</p>
    <p class="footer-email">E-mail: info@brightlanecollective.example</p>
  </footer>
</body>
</html>
```